Business Card for a mobile physiotherapy company

I need a layout for a business card for a mobile physiotherapy company.
Slogan is "Mobile Physiotherapy - Your Road To Recovery"
Phone number is 867-412-5093
Email VantePhysio@mailbox-demo.ca (subject to change with website)
Website www.VantePhysio.ca
My name and credentials: Gil Varney Gil Varney, BSc(kin), MPT, CAFCI, IMS
Information maybe included: Direct Billing, Services including Physiotherapy, IMS, acupuncture
Maybe include facebook and instagram logos
One side with the logo clean and sharp
Other side with details, try not to look too busy, keep everything concise

```html
<!DOCTYPE html>
<html lang="en">
<head>
<meta charset="utf-8">
<title>Vante Physio – Business Card</title>
<link href="https://fonts.googleapis.com/css2?family=Open+Sans:wght@400;600;700;800&display=swap" rel="stylesheet">
<style>
  :root {
    --backdrop: #2a2a2c;
    --teal-light: #136359;
    --teal-dark: #0b4a43;
    --teal-band: #0c574d;
    --navy: #2d4a7a;
    --navy-deep: #26406c;
    --paper: #ffffff;
    --ink-light: #ffffff;
  }
  * { box-sizing: border-box; margin: 0; padding: 0; }
  html, body {
    width: 1200px; height: 892px; overflow: hidden;
    background: var(--backdrop);
    font-family: "Open Sans", Arial, sans-serif;
  }
  .canvas { position: relative; width: 1200px; height: 892px; }

  .card {
    position: absolute;
    width: 540px; height: 310px;
    overflow: hidden;
    box-shadow: 0 14px 30px rgba(0,0,0,.45);
  }

  /* Front: brand side */
  .card--front {
    left: 70px; top: 100px;
    background: linear-gradient(135deg, var(--teal-light), var(--teal-dark));
    color: var(--ink-light);
  }
  .social {
    position: absolute; top: 16px; right: 18px;
    display: flex; gap: 6px;
  }
  .social__dot {
    width: 20px; height: 20px; border-radius: 50%;
    background: var(--ink-light);
  }
  .brand-mark {
    position: absolute; left: 0; right: 0; top: 100px;
    display: flex; align-items: center; justify-content: center; gap: 12px;
  }
  .brand-mark__square { width: 18px; height: 18px; background: var(--ink-light); }
  .brand-mark__name {
    font-size: 40px; font-weight: 700; letter-spacing: 2px; text-transform: uppercase;
  }
  .front-tagline {
    position: absolute; left: 0; right: 0; top: 222px;
    text-align: center; font-size: 15px; line-height: 1.45;
  }
  .front-tagline .sep { font-size: 10px; vertical-align: middle; margin: 0 4px; }

  /* Back: details side */
  .card--back {
    left: 600px; top: 480px;
    background: var(--paper);
  }
  .card__shapes { position: absolute; inset: 0; }
  .back-brand {
    position: absolute; right: 30px; top: 44px;
    display: flex; align-items: center; gap: 10px;
    color: var(--navy);
  }
  .back-brand__square { width: 14px; height: 14px; background: var(--navy); }
  .back-brand__name {
    font-size: 30px; font-weight: 700; letter-spacing: 2px; text-transform: uppercase;
  }
  .details {
    position: absolute; left: 26px; top: 168px;
    color: var(--ink-light);
  }
  .details__name { font-size: 20px; font-weight: 800; text-transform: uppercase; line-height: 1.1; }
  .details__creds, .details__billing { font-size: 13px; font-weight: 600; line-height: 1.35; }
  .contact { list-style: none; margin-top: 8px; }
  .contact__item {
    display: flex; align-items: center; gap: 9px;
    font-size: 13px; line-height: 1.5;
  }
  .contact__icon { width: 13px; height: 13px; flex: none; }
</style>
</head>
<body>
<main class="canvas">

  <section class="card card--front" aria-label="Card front">
    <div class="social" aria-label="Social media">
      <span class="social__dot"></span>
      <span class="social__dot"></span>
    </div>
    <div class="brand-mark">
      <span class="brand-mark__square"></span>
      <span class="brand-mark__name">Vante Physio</span>
    </div>
    <p class="front-tagline">
      Mobile Physiotherapy - Your Road To Recovery<br>
      Physiotherapy <span class="sep">●</span> IMS <span class="sep">●</span> Acupuncture
    </p>
  </section>

  <section class="card card--back" aria-label="Card back">
    <svg class="card__shapes" viewBox="0 0 540 310" preserveAspectRatio="none" aria-hidden="true">
      <polygon points="0,310 0,170 240,90 420,155 540,115 540,310" fill="var(--navy)"/>
      <polygon points="405,150 540,88 540,112 420,158" fill="var(--teal-band)"/>
    </svg>

    <div class="back-brand">
      <span class="back-brand__square"></span>
      <span class="back-brand__name">Vante Physio</span>
    </div>

    <div class="details">
      <h1 class="details__name">Gil Varney</h1>
      <p class="details__creds">BSc(kin), MPT, CAFCI, IMS</p>
      <p class="details__billing">Direct Billing</p>
      <ul class="contact">
        <li class="contact__item">
          <svg class="contact__icon" viewBox="0 0 16 16"><path d="M3 2h3l1.5 4-2 1.2a8 8 0 0 0 3.3 3.3L10 8.5l4 1.5v3a1 1 0 0 1-1 1A12 12 0 0 1 2 3a1 1 0 0 1 1-1z" fill="#fff"/></svg>
          867-412-5093
        </li>
        <li class="contact__item">
          <svg class="contact__icon" viewBox="0 0 16 16"><rect x="1" y="3" width="14" height="10" fill="#fff"/><path d="M1 3l7 6 7-6" fill="none" stroke="var(--navy)" stroke-width="1.4"/></svg>
          VantePhysio@mailbox-demo.ca
        </li>
        <li class="contact__item">
          <svg class="contact__icon" viewBox="0 0 16 16"><circle cx="8" cy="8" r="7" fill="#fff"/><path d="M1 8h14M8 1c-3 3.5-3 10.5 0 14M8 1c3 3.5 3 10.5 0 14" fill="none" stroke="var(--navy)" stroke-width="1"/></svg>
          www.VantePhysio.ca
        </li>
      </ul>
    </div>
  </section>

</main>
</body>
</html>
```